QVN Vision and Core Values

We are wanting to promote our core values and vision on posters at our office. I have uploaded a copy of our logo. We would like to incorporate that, the vision and the core values. ALL THREE MUST BE INCLUDED ON THE DESIGN. For reference, our website is www.qvnpetroworks.example

Our vision is:
We are a Team of Power and Strength that Builds our People and Serves our Industry and Communities.

Our Values are:
We Operate with a Standard of Excellence.
We Do the Right Thing Every Time.
We Value and Recognize our People.
We are Team Players.
We Think and Act with Optimism and Faith.

```html
<!DOCTYPE html>
<html lang="en">
<head>
<meta charset="utf-8">
<title>QVN Vision and Core Values</title>
<link href="https://fonts.googleapis.com/css2?family=Orbitron:wght@400;800;900&family=Poppins:wght@400;500;700&display=swap" rel="stylesheet">
<style>
  :root{
    --stage:#5a5a5a;
    --paper:#ffffff;
    --navy:#1d4a86;
    --navy-deep:#1b3a6b;
    --navy-bright:#1a5ba6;
    --orange:#ea8a1c;
    --orange-deep:#d9480f;
    --ink:#1e1e1e;
    --rule:#9a9a9a;
    --footer:#bdbdbd;
    --skyline:#cfcfcf;
  }
  *{margin:0;padding:0;box-sizing:border-box}
  html,body{width:832px;height:1200px;overflow:hidden;background:var(--stage)}
  .poster{position:absolute;left:26px;top:325px;width:780px;height:551px;background:var(--paper);overflow:hidden;font-family:"Poppins",sans-serif;color:var(--ink)}
  .vision-band{position:absolute;left:261px;top:0;right:0;height:187px;background:linear-gradient(180deg,var(--navy-bright),var(--navy-deep))}
  .flame-accent{position:absolute;left:226px;top:0;width:58px;height:187px;background:linear-gradient(180deg,#f0a04a,var(--orange-deep) 70%,#e65a10);border-radius:60% 0 0 100% / 40% 0 0 60%}
  .brand{position:absolute;left:35px;top:125px;width:190px;text-align:center;color:var(--navy);font-family:"Orbitron",sans-serif;font-weight:900}
  .brand-name{display:block;font-size:50px;line-height:1;letter-spacing:3px}
  .brand-sub{display:block;font-size:11.5px;letter-spacing:1.5px;margin-top:6px}
  .brand-dot{position:absolute;left:106px;top:36px;width:48px;height:48px;border-radius:50%;background:var(--navy)}
  .vision-kicker{position:absolute;left:318px;top:24px;font-family:"Orbitron",sans-serif;font-weight:900;font-size:50px;line-height:1;letter-spacing:2px;color:#fff}
  .vision-title{position:absolute;left:316px;top:72px;font-family:"Orbitron",sans-serif;font-weight:900;font-size:64px;line-height:1;letter-spacing:3px;background:linear-gradient(180deg,var(--orange),var(--orange-deep));-webkit-background-clip:text;background-clip:text;color:transparent}
  .vision-text{position:absolute;left:320px;top:136px;width:430px;font-size:14.5px;font-weight:500;line-height:1.3;color:#fff}
  .values-title{position:absolute;left:0;right:0;top:200px;text-align:center;font-family:"Orbitron",sans-serif;font-size:33px;line-height:1;color:var(--ink)}
  .values-title .light{font-weight:400}
  .values-title .bold{font-weight:900}
  .values-rule{position:absolute;left:142px;width:495px;top:240px;height:1px;background:var(--rule)}
  .value-flow{position:absolute;left:0;top:0}
  .value{position:absolute;width:150px;text-align:center;font-size:12.5px;line-height:1.3}
  .value b{font-weight:700}
  .skyline{position:absolute;left:0;right:0;top:448px;height:57px;background:var(--skyline)}
  .footer{position:absolute;left:0;right:0;bottom:0;height:46px;background:var(--footer);text-align:center;padding-top:12px;font-size:12px;font-weight:700;letter-spacing:5px;color:var(--ink)}
</style>
</head>
<body>
<main class="poster">
  <div class="vision-band"></div>
  <div class="flame-accent" role="img" aria-label="Decorative orange flame accent"></div>

  <div class="brand-dot"></div>
  <div class="brand"><span class="brand-name">QVN</span><span class="brand-sub">OILFIELD SERVICES</span></div>

  <div class="vision-kicker">OUR</div>
  <div class="vision-title">VISION</div>
  <p class="vision-text">We are a Team of Power and Strength that Builds our People and Serves our Industry and Communities.</p>

  <h2 class="values-title"><span class="light">OUR</span> <span class="bold">VALUES</span></h2>
  <div class="values-rule"></div>

  <svg class="value-flow" width="780" height="445" viewBox="0 0 780 445">
    <defs>
      <linearGradient id="blueSwoosh" x1="0" y1="1" x2="1" y2="0">
        <stop offset="0" stop-color="#1b3a6b"/><stop offset="1" stop-color="#1d5aa6"/>
      </linearGradient>
      <linearGradient id="orangeArc" x1="0" y1="0" x2="1" y2="1">
        <stop offset="0" stop-color="#f0a030"/><stop offset="1" stop-color="#d9480f"/>
      </linearGradient>
      <path id="swoosh" d="M57,378 Q150,395 198,342 L198,320 Q150,358 76,360 Z"/>
      <path id="arc" d="M190,328 Q260,270 330,345 L330,365 L318,367 Q262,305 205,346 L196,346 Z"/>
    </defs>
    <g fill="url(#blueSwoosh)">
      <use href="#swoosh"/><use href="#swoosh" x="261"/><use href="#swoosh" x="522"/>
    </g>
    <g fill="url(#orangeArc)">
      <use href="#arc"/><use href="#arc" x="261"/>
    </g>
    <g stroke="#555" stroke-width="1">
      <line x1="120" y1="308" x2="120" y2="354"/>
      <line x1="381" y1="308" x2="381" y2="354"/>
      <line x1="642" y1="308" x2="642" y2="354"/>
      <line x1="249" y1="326" x2="249" y2="383"/>
      <line x1="510" y1="326" x2="510" y2="383"/>
    </g>
    <g fill="#fff" stroke="#555" stroke-width="1">
      <circle cx="120" cy="354" r="2.5"/><circle cx="381" cy="354" r="2.5"/><circle cx="642" cy="354" r="2.5"/>
      <circle cx="249" cy="326" r="2.5"/><circle cx="510" cy="326" r="2.5"/>
    </g>
    <g fill="#fff" stroke-width="4">
      <circle cx="120" cy="285" r="22" stroke="#1d5aa6"/>
      <circle cx="381" cy="285" r="22" stroke="#1d5aa6"/>
      <circle cx="642" cy="285" r="22" stroke="#1d5aa6"/>
      <circle cx="249" cy="406" r="22" stroke="#e0761a"/>
      <circle cx="510" cy="406" r="22" stroke="#e0761a"/>
    </g>
    <g fill="none" stroke="#444" stroke-width="1.2" stroke-linecap="round" stroke-linejoin="round">
      <circle cx="120" cy="280" r="5"/><path d="M117,285 L115,291 L120,289 L125,291 L123,285"/><path d="M108,294 Q114,292 120,295 Q126,292 132,294"/>
      <rect x="371" y="277" width="20" height="14" rx="1"/><line x1="374" y1="281" x2="384" y2="281"/><line x1="374" y1="285" x2="381" y2="285"/><circle cx="387" cy="288" r="2.5"/>
      <path d="M642,292 L634,284 Q630,278 636,276 Q640,275 642,279 Q644,275 648,276 Q654,278 650,284 Z"/>
      <circle cx="249" cy="406" r="9"/><path d="M249,400 L249,406 L254,409"/>
      <circle cx="510" cy="401" r="4.5"/><path d="M501,415 Q501,407 510,407 Q519,407 519,415"/>
    </g>
  </svg>

  <p class="value" style="left:178px;top:262px">We Do the <b>Right</b><br><b>Thing Every Time</b></p>
  <p class="value" style="left:435px;top:262px">We are <b>Team</b><br><b>Players</b></p>
  <p class="value" style="left:45px;top:389px">We Operate with a<br><b>Standard of</b><br><b>Excellence</b></p>
  <p class="value" style="left:306px;top:389px">We <b>Value</b> and<br><b>Recognize</b> our<br>People</p>
  <p class="value" style="left:567px;top:389px">We Think and Act<br>with <b>Optimism</b><br><b>and Faith</b></p>

  <div class="skyline" role="img" aria-label="Grey silhouette of an industrial refinery skyline"></div>
  <footer class="footer">www.qvnpetroworks.example</footer>
</main>
</body>
</html>
```